Marla Tovesby, Broker Associate

I need a new business card for my Real Estate services. I am a Broker Associate and also have my MBA. I am a PA too. I would like to have it say "Third Generation Selling" too some where. I like the bold look of cards and I think I am leaning towards a black or dark background. I need it to tie in my logo with the Pinegate Marsden Vic Olander Realty logo. I like the foil and shiny look of some letters too. I might add my picture but would like to see some with out my picture too. I sell a lot of lakefront homes but I don't want it to be focused on water. Maybe subtle?

Target Market(s)

18+

Industry/Entity Type

Real Estate Agent

Contact Information for Business Card

The design must have my logo and Pinegate Marsden logo.
My name: Marla Tovesby
My cell phone 555-318-2976
business address: 4820 West Orchard Road Clermont, FL 34711
Office phone: 555-762-0158
email: MarlaJTovesby@mailbrook.test
website: www.BrightporchHomes.test
Facebook: www.facebook.com/marlabrightporchhomes
Also 'Third Generation Selling' and Realtor logo must be on it.

Font styles to use
Sans Serif

Colors
0555a3
000000
ffffff
d3d3d3
3176b5

Requirements
Must have
• I want this to stand out from all the other Realtors. I like bold look. I need it to match my logo and tie in the Pinegate Marsden logo. I can do front and back on card. The office details can be smaller than my name and information.
Nice to have
• I like the foil look and matte as well. I want something bold that stands out.

```html
<!DOCTYPE html>
<html lang="en">
<head>
<meta charset="utf-8">
<title>Marla Tovesby – Business Card</title>
<link rel="stylesheet" href="https://fonts.googleapis.com/css2?family=Roboto:wght@400;500;700&display=swap">
<style>
  :root {
    --backdrop: #3a332e;
    --card: #1c1e21;
    --card-edge: #121315;
    --blue: #3176b5;
    --blue-deep: #0555a3;
    --white: #ffffff;
    --silver: #d3d3d3;
    --foil: #8d9196;
  }
  * { box-sizing: border-box; margin: 0; padding: 0; }
  html, body {
    width: 1200px; height: 769px; overflow: hidden;
    background: var(--backdrop);
    font-family: "Roboto", sans-serif;
  }
  .card {
    position: absolute;
    top: 236px;
    width: 520px; height: 297px;
    background: var(--card);
    border: 1px solid var(--card-edge);
    box-shadow: 0 6px 18px rgba(0,0,0,.45);
    overflow: hidden;
  }

  /* back */
  .card--back { left: 50px; }
  .brand-mark {
    position: absolute; left: 0; right: 0; top: 100px;
    text-align: center;
    font-size: 34px; font-weight: 700; letter-spacing: 2px;
    color: var(--foil);
    text-transform: uppercase;
  }
  .tagline {
    position: absolute; left: 0; right: 0; top: 176px;
    text-align: center;
    font-size: 13px; color: var(--foil); letter-spacing: .5px;
  }
  .badges {
    position: absolute; top: 26px; right: 26px;
    display: flex; gap: 14px; align-items: flex-start;
  }
  .badge-association {
    width: 62px; height: 26px;
    border: 1px solid var(--silver);
    background: #2a2c30;
  }
  .badge-brokerage {
    width: 58px; height: 34px;
    background: var(--blue-deep);
    border: 1px solid var(--silver);
  }

  /* front */
  .card--front { left: 630px; }
  .front-mark {
    position: absolute; right: 26px; top: 62px;
    display: flex; align-items: center; gap: 8px;
    font-size: 22px; font-weight: 700; color: var(--blue);
    text-transform: uppercase; letter-spacing: 1px;
  }
  .front-mark__square { width: 14px; height: 14px; background: var(--white); }
  .contact__name {
    position: absolute; left: 26px; top: 100px;
    font-size: 19px; font-weight: 500; color: var(--blue);
    text-transform: uppercase; letter-spacing: .3px;
  }
  .divider {
    position: absolute; left: 26px; right: 26px; top: 128px;
    height: 1px; background: var(--white);
  }
  .contact__list {
    position: absolute; left: 26px; top: 136px;
    list-style: none;
  }
  .contact__list li {
    display: flex; align-items: center; gap: 8px;
    font-size: 12.5px; color: var(--white); line-height: 17px;
  }
  .contact__list svg { width: 10px; height: 10px; flex: none; }
  .divider--short { top: 212px; left: 300px; }
  .office {
    position: absolute; right: 26px; top: 220px;
    text-align: right; font-style: normal;
    font-size: 12.5px; line-height: 17px; color: var(--white);
  }
</style>
</head>
<body>

<section class="card card--back" aria-label="Card back">
  <div class="badges">
    <div class="badge-association" aria-label="Trade association badge"></div>
    <div class="badge-brokerage" aria-label="Pinegate Marsden Vic Olander Realty badge"></div>
  </div>
  <div class="brand-mark">Marla Tovesby</div>
  <p class="tagline">Third Generation Selling</p>
</section>

<section class="card card--front" aria-label="Card front">
  <div class="front-mark"><span>Marla Tovesby</span><span class="front-mark__square"></span></div>
  <h1 class="contact__name">Marla Tovesby</h1>
  <div class="divider"></div>
  <ul class="contact__list">
    <li><svg viewBox="0 0 10 10"><path fill="#3176b5" d="M2 0.5 3.6 2.6 2.7 3.6Q3.6 5.8 6.4 7.3L7.4 6.4 9.5 8 8.3 9.5Q4.5 9.2 0.5 1.7Z"/></svg>555-762-0158</li>
    <li><svg viewBox="0 0 10 10"><rect x="2.5" y="0.5" width="5" height="9" rx="1" fill="none" stroke="#3176b5"/></svg>555-318-2976</li>
    <li><svg viewBox="0 0 10 10"><rect x="0.5" y="2" width="9" height="6.5" fill="#3176b5"/><path d="M0.5 2 5 5.5 9.5 2" fill="none" stroke="#1c1e21"/></svg>MarlaJTovesby@mailbrook.test</li>
    <li><svg viewBox="0 0 10 10"><rect width="10" height="10" fill="#3176b5"/></svg>/marlabrightporchhomes</li>
  </ul>
  <div class="divider divider--short"></div>
  <address class="office">
    4820 West Orchard Road<br>
    Larkfield, FL 30917<br>
    www.BrightporchHomes.test
  </address>
</section>

</body>
</html>
```